Designer Needed for Protein Label

We are looking for an experienced graphic designer to create a label for our protein supplement Plinth PUREFORM 100% WHEY Protein 3LB tub. You can make it unique to our design but keep it clean and simple.

Here are some design examples that we liked, however please note ours is unflavored:

https://www.shopvarnel.example/BrawnLabs-Vektor-Protein-Powder-Chocolate/dp/Q07RTKZLWA/ref=sr_1_17_a_it?ie=UTF8&qid=1536255229&sr=8-17&keywords=protein%2Bpowder&th=1

https://www.shopvarnel.example/dp/Q093TLMNPX/ref=sspa_dk_detail_1?pd_rd_i=Q093TLMNPX&pf_rd_m=ZQWTYRUVN4KLM&pf_rd_p=7c4410ab-816e-4a2b-c1e7-26e4c2a0167e&pf_rd_r=HRYQLWMNT8KPRD613KJN&pd_rd_wg=KTq4h&pf_rd_s=desktop-dp-sims&pf_rd_t=40701&pd_rd_w=MQRT4&pf_rd_i=desktop-dp-sims&pd_rd_r=339f8965-c2ac-22f9-972d-de17fb2241c2&th=1

Please see attachment for Plinth Logo and additional label example.

Label Dimensions:
18in x 6in

Please include the following information on the label:
* Plinth Icon
* PUREFORM - product name
* 100% WHEY Protein
* Unflavored
* Net WT. 3LB (1.36 KG)
* 40 Servings
* 50 Grams of Protein per serving
* XX  BCAA
* Gluten & Lactose Free
* Kosher and Halal Certified
* Non GMO
* Nutrition Facts (use as place holder)
* Ingredients
* Directions
* Barcode

```html
<!DOCTYPE html>
<html lang="en">
<head>
<meta charset="utf-8">
<title>Plinth PUREFORM 100% Whey Protein – Label</title>
<link rel="stylesheet" href="https://fonts.googleapis.com/css2?family=Montserrat:wght@400;700;800;900&display=swap">
<style>
  :root {
    --page: #ffffff;
    --label-grey: #9c9c9c;
    --bar-grey: #a3a3a3;
    --ink: #0d0d0d;
    --yellow: #ffd20a;
    --white: #ffffff;
    --muted-ink: #2a2a2a;
  }
  html, body {
    margin: 0;
    padding: 0;
    width: 1200px;
    height: 1200px;
    overflow: hidden;
    background: var(--page);
  }
  .canvas {
    position: relative;
    width: 1200px;
    height: 1200px;
  }
  .label {
    position: absolute;
    left: 100px;
    top: 157px;
    width: 1000px;
    height: 886px;
    font-family: "Montserrat", sans-serif;
  }
  .label svg { display: block; width: 100%; height: 100%; }
  .field-grey { fill: var(--label-grey); }
  .field-black { fill: var(--ink); }
  .accent-yellow { fill: var(--yellow); }
  .flavor-bar { fill: var(--bar-grey); }
  .brand-name { font-weight: 900; fill: var(--ink); }
  .product-name { font-weight: 900; fill: var(--ink); }
  .title-whey { font-weight: 900; fill: var(--white); }
  .title-protein { font-weight: 800; fill: var(--yellow); }
  .flavor-text { font-weight: 400; fill: var(--muted-ink); }
  .feature-text { font-weight: 400; fill: var(--white); }
  .net-weight { font-weight: 900; fill: var(--ink); }
  .net-weight-metric { font-weight: 400; fill: var(--muted-ink); }
</style>
</head>
<body>
<div class="canvas">
  <div class="label">
    <svg viewBox="0 0 767 680" xmlns="http://www.w3.org/2000/svg" aria-label="Plinth PUREFORM 100% Whey Protein label front">
      <!-- background fields -->
      <rect class="field-grey" x="0" y="0" width="767" height="680"/>
      <polygon class="accent-yellow" points="500,67 767,15 767,2"/>
      <polygon class="field-black" points="0,165 767,15 767,545 345,672 0,612"/>
      <polygon class="accent-yellow" points="0,612 345,672 300,680 0,636"/>

      <!-- brand -->
      <rect class="accent-yellow" x="190" y="62" width="20" height="20"/>
      <text class="brand-name" x="66" y="82" font-size="40">Plinth</text>

      <!-- vertical product name band -->
      <rect class="accent-yellow" x="72" y="92" width="110" height="568"/>
      <text class="product-name" transform="translate(175,640) rotate(-90)" font-size="134" textLength="515" lengthAdjust="spacingAndGlyphs">PUREFORM</text>

      <!-- main title -->
      <text class="title-whey" x="257" y="235" font-size="160" textLength="465" lengthAdjust="spacingAndGlyphs">WHEY</text>
      <text class="title-protein" x="300" y="320" font-size="84" textLength="390" lengthAdjust="spacingAndGlyphs">PROTEIN</text>

      <!-- flavour -->
      <rect class="flavor-bar" x="255" y="335" width="470" height="43"/>
      <text class="flavor-text" x="490" y="369" font-size="30" text-anchor="middle">UNFLAVORED</text>

      <!-- feature list -->
      <g class="feature-list">
        <polygon class="accent-yellow" points="257,422 257,438 268,430"/>
        <text class="feature-text" x="277" y="439" font-size="23">40 SERVINGS</text>
        <polygon class="accent-yellow" points="257,452 257,468 268,460"/>
        <text class="feature-text" x="277" y="469" font-size="23">50 GRAMS OF PROTEIN PER SERVING</text>
        <polygon class="accent-yellow" points="257,482 257,498 268,490"/>
        <text class="feature-text" x="277" y="499" font-size="23">XX  BCAA</text>
        <polygon class="accent-yellow" points="257,512 257,528 268,520"/>
        <text class="feature-text" x="277" y="529" font-size="23">GLUTEN &amp; LACTOSE FREE</text>
        <polygon class="accent-yellow" points="257,542 257,558 268,550"/>
        <text class="feature-text" x="277" y="559" font-size="23">KOSHER AND HALAL CERTIFIED</text>
        <polygon class="accent-yellow" points="257,572 257,588 268,580"/>
        <text class="feature-text" x="277" y="589" font-size="23">NON GMO</text>
      </g>

      <!-- net weight -->
      <text class="net-weight" x="722" y="616" font-size="46" text-anchor="end" textLength="68" lengthAdjust="spacingAndGlyphs">3LB</text>
      <text class="net-weight-metric" x="722" y="637" font-size="16" text-anchor="end">(1.36 KG)</text>
    </svg>
  </div>
</div>
</body>
</html>
```